Beyond The Ledger Double Sided DL Flyer

We need a double sided flyer that we provide to a Real Estate agent for leeds. It should provide our basic services as well as a modern look and feel. The brochure should incorporate our Brand colors and have a graphic that centres around money and property. I have included a couple of pictures that we like (but have not yet purchased from PIXVAULT) as an indication of the type of picture we like.

WE need to also show the Beyond The Ledger brand and have our Phone / address's and email details.

Target Market(s)

Realestate clients (Property Investors)

Industry/Entity Type

Financial Planning

Requirements
Must have
• Picture on Front (maybe the logo on back)
• Please incorporate existing logo colours.

```html
<!DOCTYPE html>
<html lang="en">
<head>
<meta charset="utf-8">
<title>Beyond The Ledger – DL Flyer</title>
<link rel="stylesheet" href="https://fonts.googleapis.com/css2?family=Arimo:wght@400;700&display=swap">
<style>
  :root {
    --brand-green: #7cc142;
    --brand-black: #0c0c0c;
    --paper: #ffffff;
    --stage: #e4e4e2;
    --text-dark: #1a1a1a;
  }
  * { margin: 0; padding: 0; box-sizing: border-box; }
  html, body { width: 1200px; height: 1200px; overflow: hidden; }
  body { background: var(--stage); font-family: "Arimo", Arial, sans-serif; position: relative; }

  .flyer { position: absolute; top: 54px; width: 514px; height: 1092px; background: var(--paper); overflow: hidden; box-shadow: 0 4px 14px rgba(0,0,0,.18); }
  .flyer--front { left: 54px; background: var(--brand-black); }
  .flyer--back { left: 630px; }
  .flyer svg.backdrop { position: absolute; inset: 0; }

  .wordmark { position: absolute; color: var(--brand-green); font-weight: 700; text-transform: uppercase; letter-spacing: .5px; display: flex; align-items: center; gap: 12px; }
  .wordmark__square { width: 22px; height: 22px; background: var(--brand-green); flex: none; }

  .front__header { position: absolute; left: 0; top: 0; width: 514px; height: 147px; background: var(--paper); }
  .front__header .wordmark { left: 0; right: 0; top: 0; bottom: 0; justify-content: center; font-size: 40px; }

  .headline { position: absolute; font-weight: 700; font-size: 38px; line-height: 44px; text-transform: uppercase; letter-spacing: .2px; }
  .front .headline { left: 42px; top: 810px; color: var(--paper); }
  .rule { position: absolute; left: 42px; width: 432px; border-top: 1px dashed #8a8a8a; }
  .tagline { position: absolute; left: 42px; top: 930px; color: var(--brand-green); font-weight: 700; font-size: 17.5px; text-transform: uppercase; }
  .website { position: absolute; left: 42px; top: 1021px; color: var(--paper); font-weight: 700; font-size: 17px; }

  .back__wordmark { left: 0; right: 0; top: 400px; height: 36px; justify-content: center; font-size: 30px; line-height: 36px; }
  .back .headline { left: 37px; top: 531px; color: var(--brand-green); }
  .intro { position: absolute; left: 37px; top: 622px; font-size: 17px; line-height: 23px; color: var(--text-dark); }
  .specialty-tab { position: absolute; left: 37px; top: 692px; width: 226px; height: 48px; }
  .specialty-tab span { position: absolute; left: 13px; top: 13px; color: var(--paper); font-weight: 700; font-size: 19px; }
  .services { position: absolute; left: 56px; top: 758px; list-style: none; }
  .services li { display: flex; align-items: center; gap: 10px; height: 29.5px; font-size: 17.5px; color: var(--text-dark); }
  .services svg { width: 16px; height: 16px; flex: none; }

  .back__footer-rule { position: absolute; left: 0; top: 932px; width: 514px; height: 7px; background: var(--brand-green); }
  .back__footer-brand { left: 0; top: 939px; width: 202px; height: 153px; justify-content: center; font-size: 22px; line-height: 26px; }
  .back__contact { position: absolute; left: 202px; top: 939px; width: 312px; height: 153px; background: var(--brand-black); color: var(--paper); font-size: 16px; line-height: 22px; padding: 16px 0 0 18px; font-style: normal; }
</style>
</head>
<body>

<section class="flyer flyer--front front">
  <svg class="backdrop" width="514" height="1092" viewBox="0 0 514 1092">
    <defs>
      <linearGradient id="frontPhotoTone" x1="0" y1="0" x2="0" y2="1">
        <stop offset="0" stop-color="#3f7a2c"/>
        <stop offset=".55" stop-color="#6f9a4a"/>
        <stop offset=".75" stop-color="#a58564"/>
        <stop offset="1" stop-color="#b48a62"/>
      </linearGradient>
    </defs>
    <path role="img" aria-label="Photo: hand watering a seedling in a jar of coins beside coin stacks and a small house model" d="M0 147 H514 V596 C420 690 300 745 190 742 C110 740 50 710 0 668 Z" fill="url(#frontPhotoTone)"/>
    <path d="M0 668 C50 710 110 740 190 742 C300 745 420 690 514 596 L514 612 C420 710 300 762 190 760 C110 758 50 728 0 688 Z" fill="#7cc142"/>
    <path d="M170 778 C300 770 420 720 514 640 L514 648 C420 732 300 780 170 778 Z" fill="#7cc142"/>
  </svg>
  <div class="front__header">
    <div class="wordmark"><span class="wordmark__square"></span>Beyond The Ledger</div>
  </div>
  <h1 class="headline">Accountants and<br>Financial Advisors</h1>
  <div class="rule" style="top:908px"></div>
  <p class="tagline">Build your business &amp; grow your wealth</p>
  <div class="rule" style="top:972px"></div>
  <p class="website">www.beyondtheledger.com.au</p>
</section>

<section class="flyer flyer--back back">
  <svg class="backdrop" width="514" height="1092" viewBox="0 0 514 1092">
    <defs>
      <linearGradient id="backPhotoTone" x1="0" y1="0" x2="1" y2="1">
        <stop offset="0" stop-color="#c9c4bf"/>
        <stop offset=".5" stop-color="#e9e2da"/>
        <stop offset="1" stop-color="#7d8aa0"/>
      </linearGradient>
    </defs>
    <rect x="0" y="0" width="514" height="9" fill="#0c0c0c"/>
    <path role="img" aria-label="Photo: cupped hands behind a wooden house model and rising coin stacks with seedlings" d="M0 9 H514 V345 C440 380 360 392 250 392 C150 392 60 390 0 390 Z" fill="url(#backPhotoTone)"/>
    <path d="M0 420 C90 456 180 470 260 470 C370 470 450 434 514 378 L514 394 C460 452 380 492 260 494 C160 496 80 476 0 446 Z" fill="#0c0c0c"/>
    <path d="M0 446 C80 476 160 496 260 494 C380 492 460 452 514 394 L514 406 C460 468 380 506 260 508 C160 510 80 490 0 458 Z" fill="#7cc142"/>
  </svg>
  <div class="wordmark back__wordmark">Beyond The Ledger</div>
  <h2 class="headline">Accountants and<br>Financial Advisors</h2>
  <p class="intro">We do more than develop an investment strategy,<br>We also monitor the progress of each strategy.</p>
  <div class="specialty-tab">
    <svg width="226" height="48" viewBox="0 0 226 48"><path d="M0 0 H226 L208 48 H0 Z" fill="#7cc142"/><rect x="0" y="46" width="208" height="2" fill="#5e9a2e"/></svg>
    <span>We specialize in:</span>
  </div>
  <ul class="services">
    <li><svg viewBox="0 0 16 16"><rect x="1" y="3" width="12" height="12" fill="none" stroke="#7cc142" stroke-width="1.8"/><path d="M4 8 L7 11 L15 2" fill="none" stroke="#7cc142" stroke-width="2.2"/></svg>Negative Gearing &amp; Investment Properties</li>
    <li><svg viewBox="0 0 16 16"><rect x="1" y="3" width="12" height="12" fill="none" stroke="#7cc142" stroke-width="1.8"/><path d="M4 8 L7 11 L15 2" fill="none" stroke="#7cc142" stroke-width="2.2"/></svg>Property &amp; Capital Gains Tax Minimisation</li>
    <li><svg viewBox="0 0 16 16"><rect x="1" y="3" width="12" height="12" fill="none" stroke="#7cc142" stroke-width="1.8"/><path d="M4 8 L7 11 L15 2" fill="none" stroke="#7cc142" stroke-width="2.2"/></svg>Self-Managed Superannuation Funds (SMSF)</li>
    <li><svg viewBox="0 0 16 16"><rect x="1" y="3" width="12" height="12" fill="none" stroke="#7cc142" stroke-width="1.8"/><path d="M4 8 L7 11 L15 2" fill="none" stroke="#7cc142" stroke-width="2.2"/></svg>Small Business &amp; Personal Taxation</li>
    <li><svg viewBox="0 0 16 16"><rect x="1" y="3" width="12" height="12" fill="none" stroke="#7cc142" stroke-width="1.8"/><path d="M4 8 L7 11 L15 2" fill="none" stroke="#7cc142" stroke-width="2.2"/></svg>Investment Advice &amp; Risk Insurances</li>
  </ul>
  <div class="back__footer-rule"></div>
  <div class="wordmark back__footer-brand">Beyond<br>The<br>Ledger</div>
  <address class="back__contact">
    Suite 8/410 Harbourview Road<br>
    PO Box 1290, Westbay NSW 2261<br>
    P: (02) 5550 1274<br>
    E: info@beyondtheledger.com.au<br>
    ABN 12 345 678 901
  </address>
</section>

</body>
</html>
```